Kovalen Spinal Care and Performance

We need new business cards, something more modern, clean. On the back of the card maybe a quote. The Dr. likes, “The doctor of the future will give no medicine, but will interest his patient in the care of the human frame, in diet and in the cause and prevention of disease.” - Walter Brisby. We are open to other suggestions. We are a chiropractic office.

```html
<!DOCTYPE html>
<html lang="en">
<head>
<meta charset="utf-8">
<title>Kovalen Spinal Care and Performance — Business Card</title>
<link rel="stylesheet" href="https://fonts.googleapis.com/css2?family=Cormorant+SC:wght@500;600&family=Lato:wght@400;700&family=Arimo:wght@700&display=swap">
<style>
  :root {
    --backdrop: #262626;
    --paper: #ffffff;
    --ink: #1c1c1c;
    --plum: #5a2a6e;
    --plum-deep: #4f1f63;
    --lime: #a9c42a;
    --lime-bright: #c2d92e;
    --rule: #c9c9c9;
    --quote-ink: #ffffff;
  }
  * { box-sizing: border-box; margin: 0; padding: 0; }
  html, body { width: 1200px; height: 900px; overflow: hidden; }
  body {
    background: var(--backdrop);
    display: flex;
    flex-direction: column;
    align-items: center;
    justify-content: center;
    gap: 28px;
  }
  .card {
    width: 700px;
    height: 400px;
    position: relative;
    overflow: hidden;
    box-shadow: 0 12px 30px rgba(0,0,0,.45);
  }

  /* Back of card: quote */
  .card-back {
    background: linear-gradient(200deg, var(--lime-bright) 0%, #9aa531 35%, #7a5a4e 62%, var(--plum-deep) 100%);
    display: flex;
    align-items: center;
    justify-content: center;
  }
  .quote {
    width: 470px;
    color: var(--quote-ink);
    text-align: center;
    font-family: "Cormorant SC", "Times New Roman", serif;
    font-weight: 600;
    font-size: 27px;
    line-height: 1.2;
    letter-spacing: .5px;
  }
  .quote-author {
    display: block;
    text-align: right;
    font-family: "Arimo", Arial, sans-serif;
    font-weight: 700;
    font-size: 18px;
    letter-spacing: 0;
    margin-top: 2px;
    padding-right: 30px;
  }

  /* Front of card: contact */
  .card-front {
    background: var(--paper);
    display: flex;
    align-items: center;
  }
  .brand {
    width: 340px;
    display: flex;
    align-items: center;
    gap: 14px;
    padding-left: 44px;
  }
  .brand-dot {
    flex: none;
    width: 26px;
    height: 26px;
    border-radius: 50%;
    background: var(--lime);
  }
  .brand-name {
    font-family: "Lato", Arial, sans-serif;
    font-weight: 400;
    font-size: 26px;
    line-height: 1.15;
    color: var(--plum);
  }
  .divider {
    width: 1px;
    height: 230px;
    background: var(--rule);
  }
  .contact {
    padding-left: 26px;
    font-family: "Lato", Arial, sans-serif;
    color: var(--ink);
  }
  .contact-name {
    font-family: "Arimo", Arial, sans-serif;
    font-weight: 700;
    font-size: 25px;
    color: var(--plum);
    line-height: 1;
  }
  .contact-role {
    font-size: 18px;
    margin-bottom: 8px;
  }
  .contact-list { list-style: none; }
  .contact-list li {
    display: flex;
    align-items: center;
    gap: 8px;
    font-size: 19px;
    line-height: 1.35;
  }
  .contact-list svg { width: 15px; height: 15px; fill: var(--plum-deep); flex: none; }
  .web-www, .web-tld { color: var(--plum); }
  .web-domain { color: var(--lime); }
  .address {
    margin-top: 14px;
    font-size: 19px;
    line-height: 1.3;
  }
</style>
</head>
<body>

  <section class="card card-back" aria-label="Card back">
    <blockquote class="quote">
      “The doctor of the future will give no medicine but will interest his patient in the care of the human frame in diet and in the cause and prevention of disease.”
      <cite class="quote-author">-Walter Brisby</cite>
    </blockquote>
  </section>

  <section class="card card-front" aria-label="Card front">
    <div class="brand">
      <span class="brand-dot"></span>
      <span class="brand-name">Kovalen Spinal Care and Performance</span>
    </div>
    <div class="divider"></div>
    <div class="contact">
      <p class="contact-name">JONATHAN SMITH</p>
      <p class="contact-role">Managing Director</p>
      <ul class="contact-list">
        <li>
          <svg viewBox="0 0 16 16" aria-hidden="true"><path d="M2 6c0-2 2-3 6-3s6 1 6 3v1h-3V5.5H5V7H2z"/><rect x="3" y="8" width="10" height="6" rx="1"/></svg>
          044-123 456 789
        </li>
        <li>
          <svg viewBox="0 0 16 16" aria-hidden="true"><path d="M4 1h8a1 1 0 0 1 1 1v12a1 1 0 0 1-1 1H4a1 1 0 0 1-1-1V2a1 1 0 0 1 1-1zm1 2v9h6V3z"/></svg>
          044-123 456 789
        </li>
        <li>
          <svg viewBox="0 0 16 16" aria-hidden="true"><path d="M1 3h14v1L8 9 1 4zm0 3 7 5 7-5v7H1z"/></svg>
          info@kovalenspine.com
        </li>
        <li>
          <svg viewBox="0 0 16 16" aria-hidden="true"><circle cx="8" cy="8" r="7"/></svg>
          <span><span class="web-www">www.</span><span class="web-domain">kovalenspine</span><span class="web-tld">.com</span></span>
        </li>
      </ul>
      <p class="address">12345, Address Goes Here<br>Country Name, 123456.</p>
    </div>
  </section>

</body>
</html>
```